Web Design Project

Hi, we need a new and professional design for our company "partnertradehubsystem". The website should communicate business but with a friendly and professional touch.

You can use the following categories for the menu;

Home - customer groups - products - voucher system- contact

Give it your best,

Regards,
Anselm

Industry/Entity Type

Business

```html
<!DOCTYPE html>
<html lang="en">
<head>
<meta charset="utf-8">
<title>partnertradehubsystem</title>
<link rel="stylesheet" href="https://fonts.googleapis.com/css2?family=Gelasio:wght@400&family=PT+Sans:wght@400;700&display=swap">
<style>
  :root {
    --topbar-light: #6f6f6f;
    --topbar-dark: #3a3a3a;
    --nav-top: #2a2a2a;
    --nav-bottom: #050505;
    --nav-divider: #4a4a4a;
    --accent: #f39c12;
    --accent-link: #e69a0c;
    --button-top: #f5b933;
    --button-bottom: #dc9a0e;
    --button-border: #c1830a;
    --ink: #111111;
    --ink-soft: #555a60;
    --ink-muted: #8c9096;
    --page: #e9ebee;
    --white: #ffffff;
    --rule: #9a9da2;
  }
  * { margin: 0; padding: 0; box-sizing: border-box; }
  html, body { width: 1200px; height: 921px; overflow: hidden; }
  body {
    background: var(--page);
    font-family: "PT Sans", Tahoma, sans-serif;
    color: var(--ink-soft);
    position: relative;
  }
  .topbar {
    position: absolute; left: 0; top: 0; width: 1200px; height: 32px;
    background: linear-gradient(var(--topbar-light), var(--topbar-dark));
  }
  .login-field {
    position: absolute; top: 5px; height: 21px;
    background: #1e1e1e; border: 1px solid #5b5b5b; border-radius: 2px;
    color: #cfcfcf; font-size: 11px; line-height: 19px; padding-left: 5px;
  }
  .login-field.user { left: 683px; width: 140px; }
  .login-field.pass { left: 829px; width: 139px; letter-spacing: 1px; }
  .login-button {
    position: absolute; left: 975px; top: 5px; width: 64px; height: 21px;
    background: linear-gradient(#2c2c2c, #050505); border-radius: 3px;
    color: #dddddd; font-size: 11px; text-align: center; line-height: 21px;
  }
  .main-nav {
    position: absolute; left: 0; top: 32px; width: 1200px; height: 65px;
    background: linear-gradient(var(--nav-top), var(--nav-bottom));
  }
  .main-nav a {
    position: absolute; top: 0; line-height: 70px; color: var(--white);
    font-size: 14px; text-decoration: none; letter-spacing: -0.2px;
  }
  .main-nav a.active { color: var(--accent); }
  .nav-divider { position: absolute; top: 20px; width: 1px; height: 30px; background: var(--nav-divider); }
  .hero {
    position: absolute; left: 0; top: 97px; width: 1200px; height: 312px;
    background: linear-gradient(#e4e4e4 0, var(--white) 40px);
    border-bottom: 1px solid #dde0e4;
  }
  .hero-title {
    position: absolute; left: 139px; top: 31px;
    font-family: "Gelasio", Georgia, serif; font-weight: 400; font-size: 37px; color: var(--ink);
  }
  .hero-subtitle {
    position: absolute; left: 139px; top: 76px;
    font-family: "Gelasio", Georgia, serif; font-weight: 400; font-size: 26px; color: #6b6e72;
  }
  .hero-text {
    position: absolute; left: 139px; top: 152px; width: 400px;
    font-size: 15px; line-height: 25px; color: #3c4046;
  }
  .cta-band {
    position: absolute; left: 0; top: 409px; width: 1200px; height: 98px;
    background: linear-gradient(var(--white), #eceef1);
    border-bottom: 1px solid #dcdfe3;
  }
  .cta-frame {
    position: absolute; left: 139px; top: 25px; width: 207px; height: 49px;
    background: #f7f7f7; border: 1px solid #e2e2e2; border-radius: 3px;
  }
  .cta-button {
    position: absolute; left: 5px; top: 4px; width: 197px; height: 40px;
    background: linear-gradient(var(--button-top), var(--button-bottom));
    border: 1px solid var(--button-border);
    font-size: 23px; color: var(--ink); text-align: center; line-height: 40px;
  }
  .services { position: absolute; left: 139px; top: 545px; width: 900px; height: 170px; }
  .service { position: absolute; top: 0; width: 225px; }
  .service-icon { position: absolute; left: 6px; top: 10px; width: 44px; height: 32px; border-radius: 4px; }
  .service-title {
    position: absolute; left: 66px; top: 3px; white-space: nowrap;
    font-family: "Gelasio", Georgia, serif; font-weight: 400; font-size: 18px; color: var(--ink);
  }
  .service-tagline {
    position: absolute; left: 66px; top: 26px; white-space: nowrap;
    font-family: "Gelasio", Georgia, serif; font-size: 13px; color: var(--ink-muted);
  }
  .service-text {
    position: absolute; left: 0; top: 62px; width: 210px;
    font-size: 12px; line-height: 19px; color: var(--ink-soft);
  }
  .detail-button {
    position: absolute; left: 0; top: 138px; width: 88px; height: 28px;
    background: linear-gradient(var(--button-top), var(--button-bottom));
    border: 1px solid var(--button-border); border-radius: 3px;
    font-size: 13px; font-weight: 700; color: var(--ink); text-align: center; line-height: 26px;
  }
  .section-rule { position: absolute; left: 139px; top: 740px; width: 900px; border-top: 1px dashed var(--rule); }
  .column { position: absolute; top: 772px; }
  .column-title {
    font-family: "Gelasio", Georgia, serif; font-weight: 400; font-size: 29px; color: var(--ink);
    line-height: 36px; white-space: nowrap;
  }
  .update { width: 282px; padding-bottom: 12px; border-bottom: 1px dashed var(--rule); margin-bottom: 5px; }
  .update-link { display: block; margin-top: 11px; font-size: 13px; font-weight: 700; color: var(--accent-link); text-decoration: none; line-height: 19px; }
  .update-text { font-size: 12.5px; line-height: 19px; color: var(--ink-soft); }
  .update + .update { border-bottom: none; }
  .update + .update .update-link { margin-top: 0; }
  .feature-image { position: absolute; top: 46px; height: 110px; }
</style>
</head>
<body>
  <header>
    <div class="topbar">
      <div class="login-field user">username</div>
      <div class="login-field pass">••••••••</div>
      <div class="login-button">Login</div>
    </div>
    <nav class="main-nav">
      <a class="active" href="#" style="left:454px">Home</a>
      <span class="nav-divider" style="left:516px"></span>
      <a href="#" style="left:545px">Customer Groups</a>
      <span class="nav-divider" style="left:675px"></span>
      <a href="#" style="left:704px">Products</a>
      <a href="#" style="left:812px">Voucher System</a>
      <span class="nav-divider" style="left:935px"></span>
      <a href="#" style="left:964px">Contact</a>
    </nav>
  </header>

  <section class="hero">
    <h1 class="hero-title">Welcome</h1>
    <h2 class="hero-subtitle">Here you photo/text</h2>
    <p class="hero-text">Aliquam in odio ut ipsum mollis facilisis. Integer est sem, dignissim quis auctor vel, dapibus vel massa. Curabitur vulputate ligula vel mi semper tempus.</p>
  </section>

  <section class="cta-band">
    <div class="cta-frame"><div class="cta-button">Learn More</div></div>
  </section>

  <section class="services">
    <article class="service" style="left:0">
      <div class="service-icon" role="img" aria-label="Orange suitcase icon" style="background:linear-gradient(#f7a13a,#d9620c)"></div>
      <h3 class="service-title">Service One</h3>
      <p class="service-tagline">Pellentesque luctus</p>
      <p class="service-text">Donec condimentum luctus vestibulum. In fermentum, tortor sit amet fermentum euismod.</p>
      <div class="detail-button">Detail</div>
    </article>
    <article class="service" style="left:225px">
      <div class="service-icon" role="img" aria-label="Green briefcase icon" style="background:linear-gradient(#7cc24a,#4b9a28)"></div>
      <h3 class="service-title">Service Two</h3>
      <p class="service-tagline">Morbi facilisis</p>
      <p class="service-text">Duis urna tortor, sollicitudin tempus tempor et, vehicula sit amet justo. Aliquam magna sem.</p>
      <div class="detail-button">Detail</div>
    </article>
    <article class="service" style="left:450px">
      <div class="service-icon" role="img" aria-label="Blue suitcase icon" style="background:linear-gradient(#3a8fd8,#125fad)"></div>
      <h3 class="service-title">Service Three</h3>
      <p class="service-tagline">Dui vitae interdum</p>
      <p class="service-text">Cras at venenatis orci. Donec iaculis egestas orci, vel porttitor lectus consequat nec.</p>
      <div class="detail-button">Detail</div>
    </article>
    <article class="service" style="left:675px">
      <div class="service-icon" role="img" aria-label="Brown leather briefcase icon" style="background:linear-gradient(#d9793d,#a24a1c)"></div>
      <h3 class="service-title">Service Four</h3>
      <p class="service-tagline">Faucibus risus vitae</p>
      <p class="service-text">Quisque mattis facilisis orci quis volutpat. Aliquam erat volutpat. Donec mi eros, eleifend vitae nisl.</p>
      <div class="detail-button">Detail</div>
    </article>
  </section>

  <div class="section-rule"></div>

  <section class="column" style="left:139px">
    <h2 class="column-title">Latest Updates</h2>
    <div class="update">
      <a class="update-link" href="#">Donec eu orci dolor</a>
      <p class="update-text">Pellentesque in nunc quam. Sed molestie ultricies ante, vel scelerisque diam varius sed.</p>
    </div>
    <div class="update">
      <a class="update-link" href="#">Aliquam bibendum vulputate</a>
    </div>
  </section>

  <section class="column" style="left:449px">
    <h2 class="column-title">Donec urna neque</h2>
    <div class="feature-image" role="img" aria-label="Abstract golden light rays with sparkles" style="left:0;width:272px;background:linear-gradient(100deg,#5a2a0c 0%,#a8621a 45%,#f2c43a 75%,#8a4a12 100%)"></div>
  </section>

  <section class="column" style="left:758px">
    <h2 class="column-title">In venenatis sagittis</h2>
    <div class="feature-image" role="img" aria-label="Abstract orange and red flowing waves" style="left:0;width:281px;background:linear-gradient(160deg,#a8340c 0%,#e0621a 40%,#f7a12a 70%,#fbd24a 100%)"></div>
  </section>
</body>
</html>
```